50c wing mondays

We need a sign reading the following.

HEADING: (large font as the focus of the sign)

50c wing Mondays
from 6pm till late

Medium font under the picture

YOUR CHOICE
- spiced buffalo wings
- hickory smoked BBQ
- Peri Peri

Small font
conditions apply
- minimum 4 wings per serving (of the same type)
- dine in only
- no discount apply

age 18 - 35

50c wing Mondays

Character Logo
• chalkduster

000000
f37122
ffffff

• Our logo
• A picture of wings
• FONT: chalkduster
• Background: BLACK
• Font colour: ORANGE
• Logo: Attached cinder kettle logo
• every word ive stated in the project description
• HEADING MUST BE LARGE: 50c Extra large - - - WING MONDAYS: LARGE
• The rest of the working small
• clip art - too many colours

```html
<!DOCTYPE html>
<html lang="en">
<head>
<meta charset="utf-8">
<title>50c Wing Mondays</title>
<link rel="stylesheet" href="https://fonts.googleapis.com/css2?family=Schoolbell&display=block">
<style>
  :root {
    --ink: #000000;
    --flame: #f37122;
    --flame-deep: #d9691f;
    --paper: #ffffff;
    --sauce: #b5481c;
  }
  html, body {
    margin: 0;
    padding: 0;
    width: 722px;
    height: 1200px;
    overflow: hidden;
    background: var(--ink);
  }
  .sign {
    position: relative;
    width: 722px;
    height: 1200px;
    background: var(--ink);
    color: var(--flame-deep);
    font-family: "Schoolbell", "Chalkduster", "Comic Sans MS", cursive;
    overflow: hidden;
  }
  .sign * { white-space: nowrap; }

  .headline {
    position: absolute;
    left: 0;
    width: 722px;
    text-align: center;
    margin: 0;
    font-weight: 400;
    line-height: 1;
    letter-spacing: 3px;
  }
  .headline--price { top: 30px; left: -16px; font-size: 112px; }
  .headline--day { top: 118px; left: 10px; font-size: 110px; }

  .wing-photo {
    position: absolute;
    left: 157px;
    top: 262px;
    width: 410px;
    height: 300px;
    transform: rotate(-14.5deg);
    background:
      radial-gradient(ellipse 40% 28% at 50% 42%, var(--sauce) 0%, #c8622a 55%, rgba(200,98,42,0) 100%),
      radial-gradient(ellipse 48% 36% at 50% 55%, #e8e2dc 0%, var(--paper) 100%);
  }

  .flavour {
    position: absolute;
    width: 220px;
    margin: 0;
    font-size: 32px;
    line-height: 42px;
    text-align: center;
    letter-spacing: 1px;
  }
  .flavour--buffalo { left: 18px; top: 572px; }
  .flavour--peri { left: 250px; top: 590px; }
  .flavour--bbq { left: 474px; top: 572px; }

  .hours {
    position: absolute;
    top: 718px;
    left: 4px;
    width: 722px;
    text-align: center;
    font-size: 78px;
    line-height: 1;
    letter-spacing: 3px;
    margin: 0;
    font-weight: 400;
  }

  .conditions {
    position: absolute;
    top: 826px;
    left: 0;
    width: 722px;
    text-align: center;
    font-size: 33px;
    line-height: 41px;
    letter-spacing: 1.5px;
    margin: 0;
    padding: 0;
    list-style: none;
  }

  .brand {
    position: absolute;
    top: 1048px;
    left: 0;
    width: 722px;
    text-align: center;
  }
  .brand__dot {
    display: block;
    width: 28px;
    height: 28px;
    margin: 0 auto 10px;
    border-radius: 50%;
    background: var(--flame-deep);
  }
  .brand__name {
    font-size: 40px;
    line-height: 1;
    letter-spacing: 3px;
    text-transform: uppercase;
  }
</style>
</head>
<body>
  <main class="sign">
    <h1 class="headline headline--price">50c wing</h1>
    <h1 class="headline headline--day">Mondays</h1>

    <div class="wing-photo" role="img" aria-label="Photo of a plate of glazed chicken wings"></div>

    <p class="flavour flavour--buffalo">spiced<br>buffalo<br>wings</p>
    <p class="flavour flavour--peri">Peri<br>Peri</p>
    <p class="flavour flavour--bbq">hickory<br>smoked<br>BBQ</p>

    <h2 class="hours">from 6pm till late</h2>

    <ul class="conditions">
      <li>conditions apply:</li>
      <li>- minimum 4 wings per serving</li>
      <li>(of the same type)</li>
      <li>- dine in only</li>
      <li>- no discount apply</li>
    </ul>

    <div class="brand">
      <span class="brand__dot"></span>
      <span class="brand__name">Cinder Kettle</span>
    </div>
  </main>
</body>
</html>
```